Trilingual Packaging Design for Waterproof Phone Pouch (Retail Ready Box)

We are launching a new Waterproof Phone Pouch designed for beach, pool, boating, swimming, travel, and general outdoor use. It keeps your phone dry while allowing touchscreen functionality. Fits most phone sizes.

This is a new product launch—we do not have previous packaging. We are looking for creative, modern, and retail-ready box design concepts that communicate waterproof protection, durability, and lifestyle usage clearly.

Packaging Requirements:
1. Box Design Deliverables
Front, Back, Sides, Top + Bottom panels
Print-ready files (AI, PDF, EPS)
Editable working file required
3D mockups of packaging for presentation

2. Design Style
We want the design to feel:
Modern • Clean • Eye-catching
Outdoor, adventurous, travel-oriented
Premium yet affordable

We do not need the product photo on the box, as we do not currently have an HQ image of the actual product that we will be selling in the box.

(You may offer alternatives based on strong concept)

Attachements:
Two sample packaging designs
Our Logo (You may change colors of logo to match design)
Word file of trilingual content
Die-cut and dimensions of packaging box

Image of product
https://pixvault.example/Kt7wQ2z
The product color is black and yellow, as shown in the image above. It would be great if the packaging could match this color scheme.

Industry/Entity Type

Mobile Phone Accessories

Requirements
Should not have
• Image of product on packaging

```html
<!DOCTYPE html>
<html lang="en">
<head>
<meta charset="utf-8">
<title>AquaShell Floatable Waterproof Pouch – Box Dieline</title>
<link rel="stylesheet" href="https://fonts.googleapis.com/css2?family=Comfortaa:wght@700&family=Saira:wght@500;700&family=Montserrat:wght@400;500;600&display=swap">
<style>
  :root{
    --page:#cbcbcb;
    --board:#0b0b0b;
    --panel-strip:#2a2a2a;
    --yellow:#e2b52a;
    --white:#ffffff;
    --grey-text:#d9d9d9;
    --cut:#d0202a;
    --fold:#1f9a4a;
  }
  html,body{margin:0;padding:0;overflow:hidden}
  body{width:1200px;height:2329px;background:var(--page);position:relative}
  .dieline{position:absolute;left:40px;top:620px;width:1120px;height:1088px}
  .brand{font-family:"Comfortaa",sans-serif;font-weight:700;fill:var(--white)}
  .tagline{font-family:"Saira",sans-serif;font-weight:500;fill:var(--yellow);letter-spacing:.5px}
  .size-label{font-family:"Saira",sans-serif;font-weight:700;fill:var(--board)}
  .side-tag{font-family:"Montserrat",sans-serif;font-weight:500;fill:var(--white);letter-spacing:.6px}
  .heading{font-family:"Montserrat",sans-serif;font-weight:500;fill:var(--yellow)}
  .body{font-family:"Montserrat",sans-serif;font-weight:400;fill:var(--grey-text)}
  .body-strong{font-family:"Montserrat",sans-serif;font-weight:600;fill:var(--white)}
  .feature{font-family:"Montserrat",sans-serif;font-weight:500;fill:var(--white)}
  .tick{fill:var(--yellow)}
  .cut{fill:none;stroke:var(--cut);stroke-width:1}
  .fold{fill:none;stroke:var(--fold);stroke-width:1;stroke-dasharray:4 3}
  .icon-frame{fill:none;stroke:var(--yellow);stroke-width:1.2}
  .icon{fill:var(--white)}
  .icon-line{fill:none;stroke:var(--white);stroke-width:2;stroke-linecap:round}
</style>
</head>
<body>
<svg class="dieline" viewBox="0 0 1203 1168" xmlns="http://www.w3.org/2000/svg">
  <rect class="board" x="0" y="0" width="1203" height="1168" fill="var(--board)"/>

  <g class="band">
    <polygon points="0,465 140,465 155,445 230,445 262,405 511,405 638,375 950,375 1000,430 1203,430 1203,498 985,498 960,470 270,470 245,498 0,498" fill="var(--panel-strip)"/>
    <polygon points="0,375 210,375 140,465 0,465" fill="var(--yellow)"/>
    <polygon points="945,375 1203,375 1203,465 1030,465 1000,435 980,435" fill="var(--yellow)"/>
    <polyline points="40,472 120,472 158,432 220,432 262,385 320,385" fill="none" stroke="var(--yellow)" stroke-width="1.2"/>
    <polyline points="800,385 960,385 1005,440 1055,440 1078,470 1160,470" fill="none" stroke="var(--yellow)" stroke-width="1.2"/>
    <polyline points="470,355 540,375 638,375" fill="none" stroke="var(--yellow)" stroke-width="1.2"/>
  </g>

  <g class="panel-back">
    <text class="brand" x="297" y="318" font-size="70" text-anchor="middle">AquaShell</text>
    <text class="tagline" x="297" y="350" font-size="18" text-anchor="middle">FLOATABLE WATERPROOF POUCH</text>
    <text class="size-label" x="101" y="422" font-size="34">7.2"</text>

    <text class="heading" x="101" y="534" font-size="11">AquaShell Waterproof Phone Pouch</text>
    <text class="heading" x="101" y="547" font-size="11">With Arm Strap</text>
    <g class="body" font-size="7.2">
      <text x="101" y="566">Waterproof pouch for phones up to 7.2", built with</text>
      <text x="101" y="575">durable TPU. Rated IPX8 for protection up to 30m,</text>
      <text x="101" y="584">floats and shields from water, snow and dust.</text>
      <text x="101" y="593">Touchscreen works through the pouch and calls</text>
      <text x="101" y="602">can be made without removing the device.</text>
      <text x="101" y="611">Includes an adjustable arm strap for secure</text>
      <text x="101" y="620">hands-free use during swimming, running,</text>
      <text x="101" y="629">kayaking and other activities. Ideal for travel,</text>
      <text x="101" y="638">water sports &amp; outdoor use.</text>
    </g>
    <text class="heading" x="101" y="681" font-size="8">User manual</text>
    <g class="body" font-size="7.2">
      <text x="95" y="700"><tspan class="tick">✓</tspan> Test with a tissue before water use</text>
      <text x="101" y="709">to ensure waterproof seal.</text>
      <text x="95" y="727"><tspan class="tick">✓</tspan> Insert a dry phone into the pouch.</text>
      <text x="95" y="745"><tspan class="tick">✓</tspan> Seal both clips tightly.</text>
      <text x="95" y="763"><tspan class="tick">✓</tspan> Use touchscreen and calls without</text>
      <text x="101" y="772">removing the phone.</text>
      <text x="95" y="790"><tspan class="tick">✓</tspan> Rinse with clean water and dry after use.</text>
      <text x="95" y="808"><tspan class="tick">✓</tspan> Not recommended for diving deeper</text>
      <text x="101" y="817">than 30m.</text>
    </g>
    <text class="heading" x="101" y="862" font-size="7.5">Manufactured For</text>
    <text class="body-strong" x="101" y="874" font-size="9">HARBOR GOODS CO.</text>
    <text class="body" x="101" y="884" font-size="7">WWW.AQUASHELL.EXAMPLE</text>
    <text class="body" x="101" y="893" font-size="7">INFO@AQUASHELL.EXAMPLE</text>
    <text class="heading" x="101" y="932" font-size="7.5">Product Code</text>
    <text class="body" x="101" y="941" font-size="7">AS-102-72-BY</text>
    <text class="body" x="358" y="941" font-size="7" text-anchor="middle">MADE IN CHINA</text>
  </g>

  <g class="panel-side" transform="translate(578 665) rotate(-90)">
    <text class="brand" x="0" y="0" font-size="46" text-anchor="middle">AquaShell</text>
    <text class="side-tag" x="0" y="24" font-size="11" text-anchor="middle">FLOATABLE WATERPROOF POUCH</text>
  </g>
  <g class="panel-side" transform="translate(1135 665) rotate(-90)">
    <text class="brand" x="0" y="0" font-size="46" text-anchor="middle">AquaShell</text>
    <text class="side-tag" x="0" y="24" font-size="11" text-anchor="middle">FLOATABLE WATERPROOF POUCH</text>
  </g>

  <g class="panel-front">
    <text class="brand" x="853" y="318" font-size="70" text-anchor="middle">AquaShell</text>
    <text class="tagline" x="853" y="350" font-size="18" text-anchor="middle">FLOATABLE WATERPROOF POUCH</text>
    <text class="size-label" x="994" y="422" font-size="34">7.2"</text>

    <g class="feature-list">
      <rect class="icon-frame" x="660" y="408" width="42" height="42" rx="3"/>
      <path class="icon" d="M681 416 C676 426 672 432 672 437 a9 9 0 0 0 18 0 C690 432 686 426 681 416Z"/>
      <text class="feature" x="660" y="474" font-size="6.6">IPX8 WATERPROOF</text>
      <text class="feature" x="660" y="482" font-size="6.6">IMPERMEABILIDAD IPX8</text>
      <text class="feature" x="660" y="490" font-size="6.6">ÉTANCHÉITÉ IPX8</text>

      <rect class="icon-frame" x="660" y="520" width="42" height="42" rx="3"/>
      <path class="icon-line" d="M672 552 L690 552 L690 530 L682 530 L682 544"/>
      <text class="feature" x="660" y="586" font-size="6.6">INCLUDES ARM STRAP</text>
      <text class="feature" x="660" y="594" font-size="6.6">FOR SECURE FIT</text>

      <rect class="icon-frame" x="660" y="632" width="42" height="42" rx="3"/>
      <path class="icon-line" d="M680 665 L680 644 M686 665 L686 650 M674 665 L674 654"/>
      <text class="feature" x="660" y="698" font-size="6.6">TOUCH SCREEN SENSITIVITY</text>
      <text class="feature" x="660" y="706" font-size="6.6">SENSIBILIDAD DE LA PANTALLA TÁCTIL</text>
      <text class="feature" x="660" y="714" font-size="6.6">SENSIBILITÉ DE L'ÉCRAN TACTILE</text>

      <rect class="icon-frame" x="660" y="744" width="42" height="42" rx="3"/>
      <circle class="icon-line" cx="681" cy="762" r="8"/>
      <path class="icon-line" d="M668 774 q6.5 -5 13 0 t13 0"/>
      <text class="feature" x="660" y="810" font-size="6.6">FLOATABLE</text>
      <text class="feature" x="660" y="818" font-size="6.6">FLOTANTE</text>
      <text class="feature" x="660" y="826" font-size="6.6">FLOTTANTE</text>

      <rect class="icon-frame" x="660" y="856" width="42" height="42" rx="3"/>
      <path class="icon" d="M690 864 C676 866 671 878 672 890 C684 888 690 878 690 864Z"/>
      <text class="feature" x="660" y="922" font-size="6.6">LIGHTWEIGHT AND COMFORTABLE</text>
      <text class="feature" x="660" y="930" font-size="6.6">LIGERO Y CÓMODO</text>
      <text class="feature" x="660" y="938" font-size="6.6">LÉGER ET CONFORTABLE</text>
    </g>
  </g>

  <g class="flap-bottom">
    <text class="brand" x="855" y="1023" font-size="32" text-anchor="middle">AquaShell</text>
    <text class="side-tag" x="855" y="1052" font-size="12" text-anchor="middle" letter-spacing="0">Floatable Waterproof Pouch</text>
  </g>

  <g class="cut-lines">
    <path class="cut" d="M83 232 L83 20 Q83 10 93 10 L501 10 Q511 10 511 20 L511 232"/>
    <path class="cut" d="M10 77 L83 77 L83 150 L10 150 Z"/>
    <path class="cut" d="M511 77 L584 77 L584 150 L511 150"/>
    <path class="cut" d="M243 105 Q243 98 258 98 L338 98 Q353 98 353 105 L298 122 Z"/>
    <path class="cut" d="M243 196 Q243 189 258 189 L338 189 Q353 189 353 196 L298 203 Z"/>
    <path class="cut" d="M6 240 L83 232 M6 240 L6 955 L83 962"/>
    <path class="cut" d="M511 232 L526 160 L625 160 L638 232"/>
    <path class="cut" d="M642 232 L642 65 Q642 45 662 45 L1045 45 Q1065 45 1068 65 L1068 232"/>
    <path class="cut" d="M1068 232 L1082 160 L1175 160 L1195 232 L1195 962"/>
    <path class="cut" d="M511 962 L526 1035 L625 1035 L638 962"/>
    <path class="cut" d="M1068 962 L1082 1035 L1175 1035 L1195 962"/>
    <path class="cut" d="M642 962 L642 1135 Q642 1155 662 1155 L1045 1155 Q1065 1155 1068 1135 L1068 962"/>
    <path class="cut" d="M83 962 L511 962"/>
  </g>

  <g class="fold-lines">
    <line class="fold" x1="83" y1="232" x2="1195" y2="232"/>
    <line class="fold" x1="83" y1="962" x2="1195" y2="962"/>
    <line class="fold" x1="83" y1="232" x2="83" y2="962"/>
    <line class="fold" x1="511" y1="232" x2="511" y2="962"/>
    <line class="fold" x1="638" y1="232" x2="638" y2="962"/>
    <line class="fold" x1="1068" y1="232" x2="1068" y2="962"/>
    <line class="fold" x1="83" y1="72" x2="511" y2="72"/>
    <line class="fold" x1="83" y1="150" x2="511" y2="150"/>
    <line class="fold" x1="642" y1="110" x2="1068" y2="110"/>
    <line class="fold" x1="642" y1="1090" x2="1068" y2="1090"/>
  </g>
</svg>
</body>
</html>
```